Brantley Advisory Group provides support for renewable energy projects to utilities and suppliers

I need a professional looking business card that is both simple and elegant and unique. My clients are mostly large organizations not individuals. I am a consultant with my own company that is small but would like to give clients the impression I am larger. Smart grid, fiber optics, software, field hardware, distribution automation, substation automation, operations, energy storage/batteries, microgrids, customer service, strategy/roadmaps, conservation, Automated Metering Infrastruture (AMI or smart meters) are all areas of focus.

Target Market(s)

Utilities, suppliers, governmental agencies involved in energy. All types of energy especially natural gas and electrical. Especially renewable energy or green projects.

Contact Information for Business Card

Name - Mark Brantley Cell Phone - 425.318.2746 Email - mbrantley@brantleyag-example.com
Company - Brantley Advisory Group (logo) Title - Principal

Font styles to use
Serif
Sans Serif

Colors

Designer to choose colors to be used in the design.

Requirements
Must have
• Simple and professional and powerful.
• Unique/creative design.
Nice to have
• Utilize color scheme to accent logo colors. Maybe some geometric pattern on edge of card with color.
Should not have
• Busy, complicated, traditional

```html
<!DOCTYPE html>
<html lang="en">
<head>
<meta charset="utf-8">
<title>Brantley Advisory Group – Business Card</title>
<link rel="stylesheet" href="https://fonts.googleapis.com/css2?family=Open+Sans:wght@400;700;800&display=swap">
<style>
  :root {
    --stage: #1c1c1c;
    --brand-blue: #1010a0;
    --brand-blue-light: #2a2ad8;
    --brand-green: #5f9438;
    --brand-green-light: #a8e060;
    --swoosh-grey: #8c8c8c;
    --paper: #ffffff;
    --ink-light: #ffffff;
  }
  * { box-sizing: border-box; margin: 0; padding: 0; }
  html, body {
    width: 1200px;
    height: 900px;
    overflow: hidden;
    background: var(--stage);
    font-family: "Open Sans", Arial, sans-serif;
  }
  .canvas {
    width: 1200px;
    height: 900px;
    display: flex;
    flex-direction: column;
    align-items: center;
    justify-content: center;
    gap: 30px;
  }
  .card {
    position: relative;
    width: 700px;
    height: 400px;
    overflow: hidden;
    box-shadow: 0 10px 30px rgba(0,0,0,0.5);
  }

  /* Front */
  .card-front { background: var(--brand-blue); }
  .brand {
    position: absolute;
    display: flex;
    align-items: center;
    gap: 14px;
  }
  .brand-mark {
    width: 26px;
    height: 26px;
    flex: none;
  }
  .brand-name {
    font-weight: 800;
    font-size: 30px;
    line-height: 1.1;
  }
  .card-front .brand { left: 60px; top: 150px; }
  .card-front .brand-mark { background: var(--brand-green); }
  .card-front .brand-name { color: var(--ink-light); width: 260px; }
  .pattern-field {
    position: absolute;
    right: 0;
    top: 40px;
    width: 330px;
    height: 320px;
    background:
      radial-gradient(circle at 45% 50%, rgba(168,224,96,0.55), transparent 55%),
      radial-gradient(circle at 70% 30%, rgba(255,255,255,0.35), transparent 45%),
      linear-gradient(135deg, var(--brand-blue-light), var(--brand-green) 60%, var(--brand-blue-light));
    border-radius: 6px;
  }

  /* Back */
  .card-back { background: var(--paper); }
  .card-back .brand { left: 40px; top: 48px; }
  .card-back .brand-mark { background: var(--brand-blue); }
  .card-back .brand-name { color: var(--brand-blue); width: 260px; }
  .wave { position: absolute; inset: 0; width: 700px; height: 400px; }
  .contact {
    position: absolute;
    right: 50px;
    bottom: 34px;
    text-align: right;
    color: var(--ink-light);
  }
  .contact-name {
    font-weight: 700;
    font-size: 30px;
    letter-spacing: 0.5px;
    line-height: 1;
  }
  .contact-title { font-size: 18px; margin-top: 4px; }
  .contact-lines { margin-top: 18px; font-size: 17px; line-height: 1.6; }
  .contact-line {
    display: flex;
    justify-content: flex-end;
    align-items: center;
    gap: 10px;
  }
  .contact-icon { width: 20px; height: 20px; flex: none; }
</style>
</head>
<body>
<main class="canvas">

  <section class="card card-front" aria-label="Card front">
    <div class="brand">
      <span class="brand-mark"></span>
      <span class="brand-name">Brantley Advisory Group</span>
    </div>
    <div class="pattern-field" role="img" aria-label="Decorative cluster of overlapping blue, green and white squares"></div>
  </section>

  <section class="card card-back" aria-label="Card back">
    <div class="brand">
      <span class="brand-mark"></span>
      <span class="brand-name">Brantley Advisory Group</span>
    </div>

    <svg class="wave" viewBox="0 0 700 400" aria-hidden="true">
      <path d="M0,330 C120,322 240,285 330,228 C250,280 130,306 0,308 Z" fill="var(--brand-green)"/>
      <path d="M0,350 C200,325 380,185 560,175 C630,172 680,195 700,208 L700,400 L0,400 Z" fill="var(--swoosh-grey)"/>
      <path d="M0,360 C210,340 390,200 565,193 C630,191 680,212 700,224 L700,400 L0,400 Z" fill="var(--brand-blue)"/>
    </svg>

    <div class="contact">
      <p class="contact-name">MARK BRANTLEY</p>
      <p class="contact-title">Principal</p>
      <div class="contact-lines">
        <p class="contact-line">425.318.2746
          <svg class="contact-icon" viewBox="0 0 20 20" aria-hidden="true">
            <circle cx="10" cy="10" r="8.5" fill="none" stroke="var(--brand-green)" stroke-width="1.4"/>
            <path d="M7,5.5 L8.6,7.8 L7.6,9 C8.3,10.6 9.4,11.7 11,12.4 L12.2,11.4 L14.5,13 L13.6,14.6 C10,14.2 5.8,10 5.4,6.4 Z" fill="var(--brand-green)"/>
          </svg>
        </p>
        <p class="contact-line">mbrantley@brantleyag-example.com
          <svg class="contact-icon" viewBox="0 0 20 20" aria-hidden="true">
            <rect x="2" y="5" width="16" height="11" fill="none" stroke="var(--brand-green)" stroke-width="1.4"/>
            <path d="M2,5 L10,11.5 L18,5" fill="none" stroke="var(--brand-green)" stroke-width="1.4"/>
          </svg>
        </p>
      </div>
    </div>
  </section>

</main>
</body>
</html>
```